Business Card Design Project

I want a new business card for all 5 of my companies. Card needs to be double sided with my name and details on one side and all 5 logos on the other side.

Industry/Entity Type

Business

```html
<!DOCTYPE html>
<html lang="en">
<head>
<meta charset="utf-8">
<title>Harbourline Group – Business Card</title>
<link rel="stylesheet" href="https://fonts.googleapis.com/css2?family=Arimo:wght@400;700&family=Libre+Baskerville:wght@400;700&display=swap">
<style>
  :root {
    --stage: #e9e9e9;
    --card-white: #ffffff;
    --card-black: #161616;
    --ink: #1b1b1b;
    --label-light: #ececec;
    --grey-text: #8e959c;
    --rule: #c9c9c9;
    --dash: #2a2a2a;
    --green-1: #7dfc4a;
    --green-2: #c8ff52;
    --struct-green: #7ee04a;
    --caulk-blue: #6fb6f2;
    --char-yellow: #f4c82a;
    --char-blue: #3aa9e0;
  }
  * { margin: 0; padding: 0; box-sizing: border-box; }
  html, body { width: 1200px; height: 1172px; overflow: hidden; }
  body { background: var(--stage); position: relative; font-family: "Arimo", Arial, sans-serif; }

  .card { position: absolute; width: 696px; height: 398px; overflow: hidden; box-shadow: 0 2px 10px rgba(0,0,0,.18); }
  .card-front { left: 180px; top: 180px; background: var(--card-white); }
  .card-back { left: 326px; top: 596px; background: var(--card-white); }

  /* front */
  .divider { position: absolute; left: 340px; width: 1px; background: var(--rule); }
  .divider.top { top: 18px; height: 157px; }
  .divider.bottom { top: 222px; height: 158px; }
  .green-field {
    position: absolute; left: 384px; top: 0; width: 312px; height: 398px;
    background: radial-gradient(circle at 55% 35%, var(--green-1) 0%, #62f23c 45%, var(--green-2) 100%);
    border-radius: 160px 0 0 160px;
  }
  .name-bar {
    position: absolute; left: 0; top: 265px; width: 254px; height: 28px;
    background: var(--card-black); border-radius: 0 14px 14px 0;
    display: flex; align-items: center; padding-left: 58px;
  }
  .owner-name { font-family: "Libre Baskerville", Georgia, serif; font-size: 18px; color: #fff; letter-spacing: .3px; }
  .name-bar .dot { position: absolute; right: 8px; top: 6px; width: 16px; height: 16px; border: 1.5px solid #fff; border-radius: 50%; }
  .contact { position: absolute; left: 24px; top: 305px; list-style: none; }
  .contact li { display: flex; align-items: center; height: 28.5px; font-family: "Libre Baskerville", Georgia, serif; font-size: 12.5px; color: var(--ink); }
  .contact li:first-child { font-size: 10px; }
  .contact svg { width: 20px; height: 20px; margin-right: 14px; fill: none; stroke: #8a8a8a; stroke-width: 1.6; }

  /* back */
  .back-art { position: absolute; inset: 0; }
  .character { position: absolute; border-radius: 14px; }
  .char-mend { left: 76px; top: 20px; width: 100px; height: 90px; background: linear-gradient(180deg, var(--char-yellow), var(--char-blue)); }
  .char-rig { left: 216px; top: 56px; width: 126px; height: 124px; background: linear-gradient(180deg, var(--char-yellow), var(--char-blue)); }
  .char-wall { left: 283px; top: 306px; width: 56px; height: 58px; background: linear-gradient(180deg, var(--char-yellow), var(--char-blue)); }
  .char-label { position: absolute; font-weight: 700; letter-spacing: -.5px; line-height: 1; }
  .label-mend { left: 90px; top: 114px; font-size: 15px; color: var(--label-light); }
  .label-rig { left: 240px; top: 187px; font-size: 22px; color: #000; }

  .brand { position: absolute; display: flex; flex-direction: column; }
  .brand .mark { width: 30px; height: 30px; border-radius: 50%; margin-bottom: 10px; }
  .brand .name { font-weight: 700; font-size: 25px; line-height: 24px; letter-spacing: -.8px; }
  .brand .tag { font-size: 8px; margin-top: 4px; }
  .brand-structural { left: 469px; top: 24px; }
  .brand-structural .mark { background: var(--struct-green); margin-left: 28px; }
  .brand-structural .name { color: #d9d9d9; }
  .brand-structural .tag { color: #b9b9b9; }
  .brand-sealant { left: 17px; top: 258px; }
  .brand-sealant .mark { background: var(--caulk-blue); }
  .brand-sealant .name { color: var(--grey-text); }
  .brand-sealant .tag { color: #9a9a9a; }

  .brand-sitewall { position: absolute; left: 352px; top: 304px; }
  .brand-sitewall .name { font-weight: 700; font-size: 37px; color: #000; letter-spacing: -.5px; line-height: 38px; }
  .brand-sitewall .desc { font-weight: 700; font-size: 16.5px; color: #000; letter-spacing: .3px; margin-top: 2px; }
</style>
</head>
<body>

<section class="card card-front" aria-label="Business card front">
  <div class="divider top"></div>
  <div class="divider bottom"></div>
  <div class="green-field" role="img" aria-label="Soft green decorative field"></div>

  <div class="name-bar"><span class="owner-name">Owner Name</span><span class="dot"></span></div>

  <ul class="contact">
    <li>
      <svg viewBox="0 0 20 20"><path d="M6 3h3l1 4-2 1a9 9 0 0 0 4 4l1-2 4 1v3a2 2 0 0 1-2 2A13 13 0 0 1 4 5a2 2 0 0 1 2-2z"/></svg>
      08 5550 1234
    </li>
    <li>
      <svg viewBox="0 0 20 20"><rect x="2.5" y="5" width="15" height="11"/><path d="M2.5 5l7.5 6 7.5-6"/></svg>
      email@harbourline.com.au
    </li>
    <li>
      <svg viewBox="0 0 20 20"><circle cx="10" cy="10" r="8"/><path d="M2 10h16M10 2c3 3 3 13 0 16M10 2c-3 3-3 13 0 16"/></svg>
      www.harbourline.com.au
    </li>
  </ul>
</section>

<section class="card card-back" aria-label="Business card back">
  <svg class="back-art" width="696" height="398" viewBox="0 0 696 398">
    <polygon points="0,0 696,0 696,258 0,136" fill="var(--card-black)"/>
    <line x1="4" y1="181" x2="696" y2="306" stroke="var(--dash)" stroke-width="13" stroke-dasharray="30 46"/>
  </svg>

  <div class="character char-mend" role="img" aria-label="Cartoon mascot with trowel for Mr.Mend"></div>
  <span class="char-label label-mend">Mr.Mend</span>

  <div class="character char-rig" role="img" aria-label="Cartoon mascot with spanner and scaffold for Mr.Rig"></div>
  <span class="char-label label-rig">Mr.Rig</span>

  <div class="brand brand-structural">
    <span class="mark"></span>
    <span class="name">Harbourline<br>Structural</span>
    <span class="tag">A Harbourline Group Company</span>
  </div>

  <div class="brand brand-sealant">
    <span class="mark"></span>
    <span class="name">Civic<br>Sealant Services</span>
    <span class="tag">A Harbourline Group Company</span>
  </div>

  <div class="character char-wall" role="img" aria-label="Small cartoon mascot beside site fence for Mr. Sitewall"></div>
  <div class="brand-sitewall">
    <div class="name">Mr. Sitewall</div>
    <div class="desc">Construction Site Fencing</div>
  </div>
</section>

</body>
</html>
```